Financial Services General Marketing Brochure

Need a brochure to help recipients understand what makes HLC unique and the services that we offer. Must match look/feel of website https://harborlanecustody.example Layouts should make it easy to read the content - content should not be crammed into a traditional size/layout. Please see attached creative brief for specifics.

Target Market(s)

Financial advisors and mature couples looking for trustee services.

Industry/Entity Type

Financial Service

Colors
34a7d8
ffc214

Requirements
Must have
• See Creative Brief

```html
<!DOCTYPE html>
<html lang="en">
<head>
<meta charset="utf-8">
<title>Harbor Lane Custody Brochure</title>
<link href="https://fonts.googleapis.com/css2?family=Noto+Serif:wght@400;700&family=Open+Sans:wght@600&display=swap" rel="stylesheet">
<style>
  :root {
    --teal: #139fb6;
    --yellow: #f6d764;
    --ink: #2b2b2b;
    --grey-text: #555;
    --ring: #e6d3b1;
    --page-bg: #d9d9d9;
    --paper: #ffffff;
  }
  * { box-sizing: border-box; margin: 0; padding: 0; }
  html, body { width: 868px; height: 1200px; overflow: hidden; background: var(--page-bg); }
  body { position: relative; font-family: "Noto Serif", Georgia, serif; color: var(--ink); }
  .spread { position: absolute; left: 14px; top: 303px; width: 840px; height: 594px; background: var(--paper); overflow: hidden; }
  .spread-art { position: absolute; inset: 0; }
  .block { position: absolute; }
  .quote { left: 159px; top: 148px; width: 230px; font-size: 7.2px; line-height: 1.05; color: var(--grey-text); text-align: justify; }
  .quote p + p { margin-top: 3px; }
  .signature { left: 159px; top: 224px; font-size: 8.5px; color: var(--grey-text); }
  .section-title { font-size: 12.5px; color: var(--teal); letter-spacing: .3px; font-weight: 400; }
  .sub-title { font-size: 9.2px; color: var(--teal); font-weight: 400; margin-top: 4px; }
  .body-text { font-size: 7.2px; line-height: 1.02; text-align: justify; margin-top: 4px; }
  .unique { left: 14px; top: 276px; width: 188px; }
  .services { left: 435px; top: 276px; width: 236px; }
  .services ul { list-style: none; font-size: 7.2px; line-height: 1.02; margin-top: 4px; }
  .footer-line { left: 90px; top: 567px; font-size: 12px; color: #fff; }
  .brand { left: 690px; top: 546px; display: flex; align-items: center; gap: 6px; color: #fff; font-size: 11px; font-weight: 700; line-height: 1.05; }
  .brand-dot { width: 16px; height: 16px; border-radius: 50%; background: #fff; flex: none; }
  .diagram text { font-family: "Open Sans", Arial, sans-serif; font-weight: 600; fill: #2f5f8a; }
</style>
</head>
<body>
<main class="spread">
  <svg class="spread-art" viewBox="0 0 840 594" width="840" height="594">
    <defs>
      <linearGradient id="meadow" x1="0" y1="0" x2="0" y2="1">
        <stop offset="0" stop-color="#cfe3f0"/><stop offset=".45" stop-color="#dfe7a8"/><stop offset="1" stop-color="#9bb64a"/>
      </linearGradient>
      <linearGradient id="family" x1="0" y1="0" x2="1" y2="1">
        <stop offset="0" stop-color="#f4efe6"/><stop offset=".5" stop-color="#d8b79a"/><stop offset="1" stop-color="#8fae55"/>
      </linearGradient>
      <linearGradient id="skin" x1="0" y1="0" x2="0" y2="1">
        <stop offset="0" stop-color="#7a6a58"/><stop offset=".6" stop-color="#c99d84"/><stop offset="1" stop-color="#2d3f6b"/>
      </linearGradient>
      <linearGradient id="meeting" x1="0" y1="0" x2="1" y2="1">
        <stop offset="0" stop-color="#e9eef2"/><stop offset=".5" stop-color="#a87e6a"/><stop offset="1" stop-color="#6c86b0"/>
      </linearGradient>
      <linearGradient id="couple" x1="0" y1="0" x2="1" y2="1">
        <stop offset="0" stop-color="#f2f2f0"/><stop offset=".5" stop-color="#d4b59d"/><stop offset="1" stop-color="#34527e"/>
      </linearGradient>
      <radialGradient id="soft" cx=".5" cy=".4" r=".6">
        <stop offset="0" stop-color="#e8c9b3"/><stop offset="1" stop-color="#c7c3c0"/>
      </radialGradient>
    </defs>

    <rect role="img" aria-label="Photo: mother and daughter walking through a sunny meadow" x="0" y="0" width="340" height="170" fill="url(#meadow)"/>
    <rect role="img" aria-label="Photo: smiling three-generation family outdoors" x="340" y="0" width="500" height="200" fill="url(#family)"/>
    <path d="M0,135 C90,112 200,95 270,75 C340,110 430,165 540,185 C650,200 770,178 840,150 L840,594 L0,594Z" fill="var(--paper)"/>
    <path d="M230,48 C300,72 380,118 480,150 C600,186 740,170 840,125 L840,143 C740,190 600,204 480,168 C380,136 300,88 230,48Z" fill="var(--yellow)"/>
    <path d="M285,84 C345,112 410,150 500,175 C610,203 740,190 840,155 L840,165 C740,203 610,218 500,191 C410,166 345,126 285,84Z" fill="var(--teal)"/>

    <circle role="img" aria-label="Portrait photo of the firm's founder" cx="79" cy="197" r="70" fill="url(#skin)"/>
    <circle role="img" aria-label="Photo: advisor meeting with a senior client" cx="508" cy="182" r="70" fill="url(#meeting)"/>
    <circle role="img" aria-label="Photo: mature couple reviewing documents with an advisor" cx="760" cy="440" r="95" fill="url(#couple)"/>

    <g fill="var(--ink)">
      <path d="M400,154 q6,-2 6,-9 a3,3 0 1 0 -3,3 q0,4 -4,5z M408,154 q6,-2 6,-9 a3,3 0 1 0 -3,3 q0,4 -4,5z"/>
      <path d="M144,254 q6,-2 6,-9 a3,3 0 1 0 -3,3 q0,4 -4,5z M152,254 q6,-2 6,-9 a3,3 0 1 0 -3,3 q0,4 -4,5z"/>
    </g>

    <g class="diagram" font-size="5">
      <g fill="none" stroke="var(--ring)" stroke-width="1.2">
        <circle cx="251" cy="417" r="24" fill="#fff"/>
        <circle cx="381" cy="417" r="24" fill="#fff"/>
        <circle cx="279" cy="466" r="24" fill="#fff"/>
        <circle cx="356" cy="466" r="24" fill="#fff"/>
        <circle cx="318" cy="499" r="24" fill="#fff"/>
      </g>
      <circle role="img" aria-label="Photo: current beneficiary" cx="287" cy="367" r="24" fill="url(#soft)" stroke="var(--ring)"/>
      <circle role="img" aria-label="Photo: future beneficiaries" cx="343" cy="367" r="24" fill="#ecd9cc" stroke="var(--ring)"/>
      <polygon role="img" aria-label="Photo: trust creators, a senior couple" points="315,392 343,407 343,438 315,453 287,438 287,407" fill="url(#soft)"/>
      <text x="287" y="388" text-anchor="middle" font-size="3.2" fill="#fff">Current Beneficiary</text>
      <text x="343" y="388" text-anchor="middle" font-size="3.2" fill="#fff">Future Beneficiary</text>
      <text x="315" y="447" text-anchor="middle" font-size="4.5">Trust Creator</text>
      <text x="251" y="419" text-anchor="middle">Attorney</text>
      <text x="381" y="419" text-anchor="middle">Accountant</text>
      <text x="279" y="468" text-anchor="middle">Financial</text>
      <text x="356" y="468" text-anchor="middle">Trustee</text>
      <text x="318" y="490" text-anchor="middle" font-size="4.3">Human Capital</text>
      <text x="318" y="495" text-anchor="middle" font-size="4.3">Resources</text>
      <g font-size="2.6" fill="#777" text-anchor="middle">
        <text x="318" y="500">Legacy Planning</text>
        <text x="318" y="503.5">Care Management</text>
        <text x="318" y="507">Philanthropy</text>
        <text x="318" y="510.5">Life Coaching</text>
      </g>
    </g>

    <path d="M0,512 C220,548 520,560 840,508 L840,594 L0,594Z" fill="var(--teal)"/>
  </svg>

  <div class="block quote">
    <p>We understand that wealth and families is very complex. As families try to transfer wealth it can be an incredible blessing or, if done improperly, can be incredibly destructive. Often a neutral third party is needed to come alongside the family's advisory team to provide guidance as families go through their wealth transition.</p>
    <p>Our relational focus, and Open Framework approach, helps families to successfully navigate through the complexities of wealth, family and trusts. We believe a family “legacy” is about more than just money.</p>
  </div>
  <div class="block signature">Daniel Whitcombe, J.D.</div>

  <section class="block unique">
    <h2 class="section-title">WHAT MAKES HLC UNIQUE</h2>
    <h3 class="sub-title">1. Responsive</h3>
    <p class="body-text">The family deals directly with decision makers instead of being subject to committees with whom the family may never have the opportunity to interact or engage.</p>
    <h3 class="sub-title">2. Family Focus</h3>
    <p class="body-text">We help families successfully navigate the complexities of family wealth, not just perform trust administration.</p>
    <h3 class="sub-title">3. Independent</h3>
    <p class="body-text">To avoid any conflicts of interest, we have no formal affiliations with wealth management firms or financial advisory practices.</p>
    <h3 class="sub-title">4. Customized</h3>
    <p class="body-text">Together we develop a customized approach that will best suit the family's needs.</p>
  </section>

  <section class="block services">
    <h2 class="section-title">OUR SERVICES</h2>
    <h3 class="sub-title">What We Offer</h3>
    <p class="body-text">We specialize exclusively in the delivery of trustee and estate fiduciary services.</p>
    <h3 class="sub-title">Who We Serve</h3>
    <ul><li>Families</li><li>Professional Advisors</li><li>Foundations</li></ul>
    <h3 class="sub-title">How We Serve</h3>
    <p class="body-text">Our expertise and experience is in family wealth. In this regard, we serve in the following ways:</p>
    <ul>
      <li>o Trustee (Trusts)</li><li>o Executor and Personal Representative (Will)</li><li>o Agent for Financial Affairs (Power of Attorney)</li><li>o Trust Protector</li><li>o Special Independent Trustee</li><li>o Consultant</li><li>o Expert Witness</li>
    </ul>
    <h3 class="sub-title">Trust Specialties</h3>
    <p class="body-text">The general types of trusts on which we serve as trustee:</p>
    <ul>
      <li>o Family Trusts</li><li>o Charitable Trusts</li><li>o Family Foundations</li><li>o Life Insurance Trusts</li><li>o Retirement Trusts</li><li>o Special Needs Trusts</li>
    </ul>
  </section>

  <div class="block footer-line">Harbor Lane Custody Client/Family Centered Team</div>
  <div class="block brand"><span class="brand-dot"></span><span>Harbor Lane<br>Custody</span></div>
</main>
</body>
</html>
```